colour scheme is to be grey background and light green writing
i would like some kind of brick arch highlighted in green and the writing inside the arch in green also
on the back list..all types of brickwork, no job to small, free quote and space to write a small quote underneath

RMT Brickwork
0491582307
keltonmarsh47@brickmailer.net

```html
<!DOCTYPE html>
<html lang="en">
<head>
<meta charset="utf-8">
<title>RMT Brickwork – Business Card</title>
<link rel="stylesheet" href="https://fonts.googleapis.com/css2?family=Arvo:wght@400;700&display=swap">
<style>
  :root {
    --page-bg: #e9e7e3;
    --card-grey: #424242;
    --brick-green: #4fc02a;
    --arch-tone-light: #4f7a3c;
    --arch-tone-dark: #435a39;
    --line-dark: #3a3a3a;
  }
  * { box-sizing: border-box; margin: 0; padding: 0; }
  html, body {
    width: 1200px;
    height: 900px;
    overflow: hidden;
  }
  body {
    background: var(--page-bg);
    font-family: "Arvo", Georgia, serif;
    position: relative;
  }
  .card {
    position: absolute;
    left: 270px;
    width: 660px;
    height: 377px;
    background: var(--card-grey);
    box-shadow: 0 6px 18px rgba(0,0,0,0.25);
    overflow: hidden;
  }
  .card--back { top: 52px; }
  .card--front { top: 471px; }

  /* Back side */
  .services {
    list-style: none;
    position: absolute;
    top: 62px;
    left: 0;
    right: 0;
    text-align: center;
    color: var(--brick-green);
    font-size: 19px;
    letter-spacing: 1.5px;
    text-transform: uppercase;
  }
  .services li { margin-bottom: 22px; }
  .quote-bar {
    position: absolute;
    left: 130px;
    right: 42px;
    top: 238px;
    height: 62px;
    background: var(--brick-green);
  }
  .quote-bar__line {
    position: absolute;
    left: 40px;
    right: 30px;
    top: 42px;
    height: 2px;
    background: var(--line-dark);
  }

  /* Front side */
  .arch-artwork {
    position: absolute;
    inset: 0;
    width: 100%;
    height: 100%;
  }
  .identity {
    position: absolute;
    left: 192px;
    top: 112px;
    width: 320px;
    text-align: center;
    color: var(--brick-green);
  }
  .identity__name {
    font-size: 26px;
    font-weight: 700;
    line-height: 1.1;
    letter-spacing: 1px;
    margin-bottom: 12px;
  }
  .identity__contact {
    font-size: 16px;
    line-height: 1.5;
    letter-spacing: 0.5px;
  }
</style>
</head>
<body>

  <section class="card card--back" aria-label="Card back">
    <ul class="services">
      <li>All types of brickwork</li>
      <li>No job to small</li>
      <li>Free quote</li>
    </ul>
    <div class="quote-bar"><div class="quote-bar__line"></div></div>
  </section>

  <section class="card card--front" aria-label="Card front">
    <svg class="arch-artwork" viewBox="0 0 660 377" role="img" aria-label="Green line illustration of a brick arch on pillars set in a brick wall, framing the card text">
      <defs>
        <linearGradient id="archTone" x1="0" y1="0" x2="1" y2="1">
          <stop offset="0%" stop-color="var(--arch-tone-light)"/>
          <stop offset="100%" stop-color="var(--arch-tone-dark)"/>
        </linearGradient>
      </defs>
      <path fill="url(#archTone)" fill-rule="evenodd"
            d="M0 0 H660 V377 H0 Z
               M165 377 V235 A187 187 0 0 1 539 235 V377 Z"/>
    </svg>
    <div class="identity">
      <h1 class="identity__name">RMT<br>Brickwork</h1>
      <p class="identity__contact">0491582307<br>keltonmarsh47@brickmailer.net</p>
    </div>
  </section>

</body>
</html>
```